Online retailer needs a Quirky yet professionally designed double sided business car

We mainly sell kitchen and home accessories but pretty much anything new and in demand. Have a look at our site and then come up with designs.
Design to be really catching and want people to visit the website.
Final details such as number, director name and email address will be given to the designer of the winning business card.

Www.zapfinda.com

Ideas out of the norm also welcome!!

```html
<!DOCTYPE html>
<html lang="en">
<head>
<meta charset="utf-8">
<title>Zapfinda – Business Card</title>
<link rel="stylesheet" href="https://fonts.googleapis.com/css2?family=Questrial&display=swap">
<style>
  :root {
    --page: #ffffff;
    --orange: #f38831;
    --white: #ffffff;
    --ink: #1c1c1c;
    --mark: #b97b66;
    --detail: #d9a07a;
    --url: #9c5a3e;
    --tagline: #f38831;
    --rule: #9a9a9a;
    --edge: #2a2a2a;
  }
  * { margin: 0; padding: 0; box-sizing: border-box; }
  html, body {
    width: 927px;
    height: 1200px;
    overflow: hidden;
    background: var(--page);
    font-family: "Questrial", sans-serif;
  }
  .canvas {
    position: relative;
    width: 927px;
    height: 1200px;
  }
  .card {
    position: absolute;
    left: 192px;
    width: 550px;
    height: 306px;
    background: var(--orange);
    border: 1px solid var(--edge);
    box-shadow: 7px 8px 7px rgba(0, 0, 0, 0.35);
    overflow: hidden;
  }
  .card--front { top: 235px; }
  .card--back { top: 617px; }

  .front-header {
    position: absolute;
    left: 0; top: 0;
    width: 100%;
    height: 101px;
    background: var(--white);
  }
  .brand-name {
    position: absolute;
    left: 0; top: 36px;
    width: 100%;
    text-align: center;
    font-size: 36px;
    line-height: 1;
    color: var(--ink);
    letter-spacing: 0.5px;
  }
  .brand-tagline {
    position: absolute;
    left: 0; top: 81px;
    width: 100%;
    display: flex;
    justify-content: center;
    align-items: center;
    gap: 6px;
    font-size: 10px;
    color: var(--tagline);
  }
  .brand-tagline::before,
  .brand-tagline::after {
    content: "";
    width: 38px;
    height: 1px;
    background: var(--rule);
  }

  .mark-circle {
    position: absolute;
    border-radius: 50%;
    background: var(--mark);
    opacity: 0.85;
  }
  .card--front .mark-circle {
    left: 460px; top: 170px;
    width: 92px; height: 92px;
  }
  .card--back .mark-circle {
    left: 226px; top: 90px;
    width: 96px; height: 96px;
  }

  .contact {
    position: absolute;
    left: 34px; top: 233px;
    list-style: none;
    font-size: 11px;
    line-height: 15px;
    color: var(--detail);
  }

  .website {
    position: absolute;
    left: 0; top: 270px;
    width: 100%;
    text-align: center;
    font-size: 13px;
    letter-spacing: 2.5px;
    color: var(--url);
  }
</style>
</head>
<body>
  <main class="canvas">
    <section class="card card--front" aria-label="Business card front">
      <header class="front-header">
        <h1 class="brand-name">Zapfinda</h1>
        <p class="brand-tagline">accessorise your needs</p>
      </header>
      <div class="mark-circle" aria-hidden="true"></div>
      <ul class="contact">
        <li>Address: Text text text text</li>
        <li>Tel.: +00 000 000 00 00</li>
        <li>Mob.:+00 000 000 00 00</li>
        <li>e-mail: office@name.com</li>
      </ul>
    </section>

    <section class="card card--back" aria-label="Business card back">
      <div class="mark-circle" aria-hidden="true"></div>
      <p class="website">Www.zapfinda.com</p>
    </section>
  </main>
</body>
</html>
```